KTRL Business Card Design

Business card for sole operator professional civil and traffic engineer.
Clients are developers and planners who require assistance with traffic strategic master planning advice and design development for access and infrastructure associated with the development.
Colours already in use are greens for the business name and black for other legend. The attached file shows the letterhead template which is currently in use.
Target Market(s)
Professional Clients in development industry
Most clients known to the Principal and card is mostly required to allow ongoing contact
Industry/Entity Type
Business
Contact Information for Business Card
DONALD PLUMWEATHER ADVISORY SERVICES
ABN 37 806 519 174
PO Box 718 KELVALE NSW 2461
Donald Plumweather 0413 885 190
donald.plumweather@farvenmail.com

```html
<!DOCTYPE html>
<html lang="en">
<head>
<meta charset="utf-8">
<title>KTRL Business Card</title>
<link rel="stylesheet" href="https://fonts.googleapis.com/css2?family=Arimo:wght@700&family=Arvo:wght@700&display=swap">
<style>
  :root {
    --backdrop: #000000;
    --card-light: #ffffff;
    --card-shade: #e6e8e8;
    --brand-green: #22c704;
    --ink: #141414;
  }
  html, body {
    margin: 0;
    width: 1200px;
    height: 900px;
    overflow: hidden;
    background: var(--backdrop);
  }
  .card {
    position: absolute;
    left: 31px;
    top: 142px;
    width: 1125px;
    height: 674px;
    overflow: hidden;
    background: radial-gradient(ellipse at 60% 40%, var(--card-light) 0%, #f5f6f6 45%, var(--card-shade) 100%);
  }
  .card__band {
    position: absolute;
    left: 0;
    top: 0;
    width: 1125px;
    height: 674px;
  }
  .card__business-name {
    position: absolute;
    left: 0;
    width: 1125px;
    top: 338px;
    margin: 0;
    text-align: center;
    font-family: "Arimo", Arial, sans-serif;
    font-weight: 700;
    font-size: 44px;
    letter-spacing: 0.3px;
    color: var(--brand-green);
    white-space: nowrap;
  }
  .card__contact {
    position: absolute;
    left: 458px;
    top: 438px;
    margin: 0;
    font-family: "Arvo", Georgia, serif;
    font-weight: 700;
    font-size: 27px;
    line-height: 46px;
    color: var(--ink);
    font-style: normal;
    white-space: nowrap;
  }
</style>
</head>
<body>
  <section class="card">
    <svg class="card__band" viewBox="0 0 1125 674" role="img" aria-label="Green curved band across the top of the card">
      <path d="M0 0 H1125 V72 C920 -5 720 40 570 135 C420 230 250 292 0 282 Z" fill="var(--brand-green)"/>
    </svg>

    <h1 class="card__business-name">DONALD PLUMWEATHER ADVISORY SERVICES</h1>

    <address class="card__contact">
      ABN 37 806 519 174 PO<br>
      Box 718 KELVALE NSW 2461<br>
      Donald Plumweather 0413 885 190<br>
      donald.plumweather@farvenmail.com
    </address>
  </section>
</body>
</html>
```